harbor institute of business and technology web site

I need web site for the institute which focus on business courses and computer course it is also for vocation train for employment It is also carear development and advancement .It should have links to online study resource which free
Industry/Entity Type
Business
Number of Pages Required
1 page
Look and feel
Each slider illustrates characteristics of the customer's brand and the style your logo design should communicate.

```html
<!DOCTYPE html>
<html lang="en">
<head>
<meta charset="utf-8">
<title>Harbor Institute of Business and Technology</title>
<link href="https://fonts.googleapis.com/css2?family=Open+Sans:wght@400;600;700;800&display=swap" rel="stylesheet">
<style>
:root{
  --blue:#22a6e3;
  --blue-dark:#1790c9;
  --ink:#333a40;
  --muted:#7a8288;
  --light:#f0f2f4;
  --night:#1e2a33;
  --white:#ffffff;
}
*{box-sizing:border-box;margin:0;padding:0}
html,body{width:1200px;height:2416px;overflow:hidden}
body{font-family:"Open Sans",Arial,sans-serif;color:var(--ink);background:var(--white);font-size:14px}
.wrap{width:780px;margin:0 auto;position:relative}

/* hero */
.hero{height:520px;position:relative;background:linear-gradient(160deg,#9aa5ad 0%,#c9cfd3 40%,#7d8891 100%);overflow:hidden}
.hero-photo{position:absolute;inset:0;background:linear-gradient(180deg,rgba(40,55,70,.35),rgba(20,30,40,.15) 60%,rgba(20,30,40,.4))}
.topbar{position:absolute;top:0;left:0;right:0;height:100px}
.brand{position:absolute;left:112px;top:0;width:96px;height:100px;background:var(--white);display:flex;flex-direction:column;align-items:center;justify-content:center;gap:8px}
.brand-mark{width:36px;height:36px;background:var(--blue)}
.brand-name{font-size:11px;font-weight:700;color:var(--blue);text-transform:uppercase;letter-spacing:.5px}
.nav{position:absolute;right:70px;top:44px;display:flex;gap:22px;list-style:none}
.nav li{color:var(--white);font-size:13px;font-weight:700;letter-spacing:.5px}
.hero-title{position:absolute;top:250px;left:0;right:0;text-align:center;color:var(--white)}
.hero-title h1{font-size:56px;font-weight:800;letter-spacing:2px;line-height:1}
.hero-title p{font-size:34px;font-weight:800;margin-top:14px;letter-spacing:.5px}
.dots{position:absolute;top:458px;left:0;right:0;display:flex;justify-content:center;gap:8px}
.dots span{width:12px;height:12px;border-radius:50%;background:rgba(255,255,255,.6)}
.dots span.on{background:var(--blue)}

/* welcome */
.welcome{height:540px;background:var(--blue);color:var(--white);padding-top:44px;text-align:center}
.welcome h2{font-size:18px;font-weight:700;letter-spacing:.3px}
.welcome .lead{font-size:11px;line-height:17px;width:620px;margin:16px auto 0;opacity:.95}
.features{display:flex;justify-content:space-between;margin-top:52px}
.feature{width:170px}
.feature .icon{width:100px;height:100px;border-radius:50%;background:var(--white);margin:0 auto;display:flex;align-items:center;justify-content:center}
.feature h3{font-size:13px;font-weight:700;margin-top:22px;text-transform:uppercase}
.feature p{font-size:11px;line-height:17px;margin-top:10px;opacity:.95}
.more{display:inline-block;font-size:11px;font-weight:700;margin-top:18px;text-transform:uppercase}

/* courses */
.courses{height:620px;padding-top:44px}
.section-title{font-size:18px;font-weight:700;text-align:center;text-transform:uppercase}
.course-grid{display:flex;justify-content:space-between;margin-top:40px}
.course{width:370px}
.course-photo{height:300px;background:linear-gradient(135deg,#b9c6d0,#e6ebee 55%,#8fa3b2)}
.course h3{font-size:12px;font-weight:700;color:var(--blue);text-transform:uppercase;margin-top:20px}
.course p{font-size:11px;line-height:17px;color:var(--muted);margin-top:8px}
.course .more{color:var(--blue)}

/* info */
.info{height:380px;background:var(--light);padding-top:40px}
.info-grid{display:flex;justify-content:space-between}
.info-col{width:240px}
.info-col h4{font-size:14px;font-weight:700;text-transform:uppercase;margin-bottom:18px}
.bullets{list-style:none}
.bullets li{font-size:11px;color:var(--muted);line-height:22px;display:flex;align-items:center;gap:8px}
.bullets li::before{content:"";width:6px;height:6px;background:var(--blue);flex:none}
.news-item{display:flex;gap:12px;margin-bottom:16px}
.date{width:64px;flex:none;background:var(--blue);color:var(--white);text-align:center;font-weight:700;font-size:13px;line-height:22px}
.date span{display:block;background:var(--blue-dark);font-size:11px}
.news-item p{font-size:11px;line-height:16px;color:var(--blue)}

/* footer */
.footer{height:280px;background:var(--blue);color:var(--white);padding-top:34px}
.footer-grid{display:flex;justify-content:space-between}
.footer h4{font-size:14px;font-weight:700;text-transform:uppercase;margin-bottom:20px}
.testimonial{width:200px}
.quote{background:var(--blue-dark);padding:18px;font-size:11px;line-height:17px;display:flex;gap:10px}
.quote .mark{width:20px;height:20px;background:var(--white);opacity:.6;flex:none}
.quote-link{font-size:11px;font-weight:700;text-align:center;margin-top:10px}
.newsletter{width:280px}
.fields{display:flex;gap:10px}
.field{height:30px;flex:1;background:var(--white);color:#9aa;font-size:11px;padding:7px 10px}
.field.msg{height:56px;margin-top:10px}
.btn{display:inline-block;margin-top:14px;background:var(--night);font-size:11px;font-weight:700;padding:8px 16px;text-transform:uppercase}
.contact{width:200px}
.contact-row{display:flex;gap:10px;font-size:11px;line-height:16px;margin-bottom:12px;align-items:flex-start}

/* bottom */
.bottom{height:76px;background:var(--night);color:#c3ccd2}
.bottom .wrap{height:76px;display:flex;align-items:center;justify-content:space-between}
.bottom p{font-size:11px}
.social{display:flex;gap:10px}
.social span{width:32px;height:32px;border-radius:50%;border:2px solid #c3ccd2}
</style>
</head>
<body>

<header class="hero">
  <div class="hero-photo" role="img" aria-label="Photo of a student writing notes at a desk"></div>
  <div class="topbar">
    <div class="brand"><div class="brand-mark"></div><div class="brand-name">Harbor</div></div>
    <ul class="nav">
      <li>HOME</li><li>ABOUT US</li><li>ADMISSION</li><li>COURSES ▾</li><li>PROGRAMS</li><li>NEWS</li><li>CONTACT US</li>
    </ul>
  </div>
  <div class="hero-title">
    <h1>HARBOR</h1>
    <p>INSTITUTE OF BUSINESS AND TECHNOLOGY</p>
  </div>
  <div class="dots"><span></span><span class="on"></span><span></span></div>
</header>

<section class="welcome">
  <div class="wrap">
    <h2>WELCOME TO HARBOR INSTITUTE OF BUSINESS AND TECHNOLOGY</h2>
    <p class="lead">Harbor Institute of Business and Technology is a fast growing education and training centre offering practical business and computer courses, vocational training for employment and career development. It is built on the belief that skills and knowledge create real opportunities for every learner and every community we serve.</p>
    <div class="features">
      <div class="feature">
        <div class="icon"><svg width="46" height="46" viewBox="0 0 46 46"><path d="M30 6a10 10 0 0 0-9 14L7 34l5 5 14-14a10 10 0 0 0 14-9l-6 6-6-2-2-6z" fill="var(--blue)"/></svg></div>
        <h3>Technical Education</h3>
        <p>Hands-on technical programs that prepare students for professional careers and real workplace demands.</p>
        <span class="more">Read more &gt;&gt;</span>
      </div>
      <div class="feature">
        <div class="icon"><svg width="46" height="46" viewBox="0 0 46 46"><circle cx="23" cy="18" r="11" fill="var(--blue)"/><rect x="17" y="28" width="12" height="8" fill="var(--blue)"/><rect x="19" y="38" width="8" height="3" fill="var(--blue)"/></svg></div>
        <h3>Ductivity</h3>
        <p>Practical learning methods that build productive habits and prepare students for modern workplaces.</p>
        <span class="more">Read more &gt;&gt;</span>
      </div>
      <div class="feature">
        <div class="icon"><svg width="46" height="46" viewBox="0 0 46 46"><rect x="6" y="26" width="7" height="14" fill="var(--blue)"/><rect x="16" y="18" width="7" height="22" fill="var(--blue)"/><rect x="26" y="10" width="7" height="30" fill="var(--blue)"/><rect x="36" y="20" width="5" height="20" fill="var(--blue)"/></svg></div>
        <h3>Performance</h3>
        <p>Measured results and steady progress tracking that help students reach strong professional performance.</p>
        <span class="more">Read more &gt;&gt;</span>
      </div>
      <div class="feature">
        <div class="icon"><svg width="46" height="46" viewBox="0 0 46 46"><circle cx="18" cy="20" r="9" fill="none" stroke="var(--blue)" stroke-width="5" stroke-dasharray="4 3"/><circle cx="18" cy="20" r="4" fill="var(--blue)"/><circle cx="33" cy="33" r="6" fill="none" stroke="var(--blue)" stroke-width="4" stroke-dasharray="3 2"/></svg></div>
        <h3>Skill Development</h3>
        <p>Focused skill building courses that support career development and long term advancement for learners.</p>
        <span class="more">Read more &gt;&gt;</span>
      </div>
    </div>
  </div>
</section>

<section class="courses">
  <div class="wrap">
    <h2 class="section-title">Our Courses</h2>
    <div class="course-grid">
      <article class="course">
        <div class="course-photo" role="img" aria-label="Photo of a business class with a presenter at a board"></div>
        <h3>Business Course</h3>
        <p>Harbor Institute of Business and Technology is a fast growing education and training centre offering practical business courses. Students gain management, accounting and marketing skills that lead to employment and career growth in every sector.</p>
        <span class="more">Read more &gt;&gt;</span>
      </article>
      <article class="course">
        <div class="course-photo" role="img" aria-label="Photo of students working at computers in a lab"></div>
        <h3>Computer Course</h3>
        <p>Harbor Institute of Business and Technology offers computer training from basic office skills to networking and programming. Courses combine guided lab practice with free online study resources so learners can progress at their own pace.</p>
        <span class="more">Read more &gt;&gt;</span>
      </article>
    </div>
  </div>
</section>

<section class="info">
  <div class="wrap info-grid">
    <div class="info-col">
      <h4>Technology Capabilities</h4>
      <ul class="bullets">
        <li>Modern computer labs with internet</li>
        <li>Online platform for free study resources</li>
        <li>Library of business and IT titles</li>
        <li>Interactive learning experience</li>
        <li>Networking and hardware practice</li>
        <li>Office tools and accounting software</li>
        <li>Experienced teaching staff</li>
        <li>Career guidance and job placement</li>
      </ul>
    </div>
    <div class="info-col">
      <h4>Our Programs</h4>
      <ul class="bullets">
        <li>Undergraduate degree program (4 years)</li>
        <li>Masters degree program</li>
        <li>Post graduate diploma (1 year)</li>
        <li>Certificate program (1 year)</li>
        <li>Diploma level program (2 years)</li>
        <li>Advanced diploma (3 years)</li>
        <li>Short business courses</li>
        <li>Vocational training for employment</li>
      </ul>
    </div>
    <div class="info-col">
      <h4>News</h4>
      <div class="news-item"><div class="date">SEP 24<span>2015</span></div><p>New semester intake now open for business and computer courses this autumn</p></div>
      <div class="news-item"><div class="date">SEP 24<span>2015</span></div><p>Free online study resources added to the student portal for all programs</p></div>
      <div class="news-item"><div class="date">SEP 24<span>2015</span></div><p>Career development workshop scheduled with local employers next month</p></div>
    </div>
  </div>
</section>

<footer class="footer">
  <div class="wrap footer-grid">
    <div class="testimonial">
      <h4>Testimonials</h4>
      <div class="quote"><span class="mark"></span><p>The courses gave me practical skills and helped me find my first job quickly.</p></div>
      <p class="quote-link">Read More &gt;&gt;</p>
    </div>
    <div class="newsletter">
      <h4>Newsletter Subscription</h4>
      <div class="fields"><div class="field">Name</div><div class="field">Email</div></div>
      <div class="field msg">Message</div>
      <span class="btn">Subscribe</span>
    </div>
    <div class="contact">
      <h4>Contact Us</h4>
      <div class="contact-row"><svg width="14" height="16" viewBox="0 0 14 16"><path d="M7 0a6 6 0 0 0-6 6c0 4 6 10 6 10s6-6 6-10a6 6 0 0 0-6-6z" fill="#fff"/><circle cx="7" cy="6" r="2" fill="var(--blue)"/></svg><span>12 Harbor Lane, Port Ellis 40210</span></div>
      <div class="contact-row"><svg width="14" height="14" viewBox="0 0 14 14"><path d="M3 0l3 3-2 2a8 8 0 0 0 5 5l2-2 3 3-2 3C6 14 0 8 0 3z" fill="#fff"/></svg><span>+1 (555) 014-2290</span></div>
      <div class="contact-row"><svg width="14" height="14" viewBox="0 0 14 14"><path d="M3 0l3 3-2 2a8 8 0 0 0 5 5l2-2 3 3-2 3C6 14 0 8 0 3z" fill="#fff"/></svg><span>+1 (555) 014-2291</span></div>
      <div class="contact-row"><svg width="14" height="12" viewBox="0 0 14 12"><rect width="14" height="12" fill="#fff"/><path d="M0 0l7 6 7-6" stroke="var(--blue)" fill="none"/></svg><span>info@harborinstitute.example</span></div>
    </div>
  </div>
</footer>

<div class="bottom">
  <div class="wrap">
    <p>Copyright © 2015 Harbor Institute of Business and Technology. All right reserved.</p>
    <div class="social"><span></span><span></span><span></span><span></span></div>
  </div>
</div>

</body>
</html>
```